Price sign

Looking for a fresh new pricing sign.. with new prices size 2ft tall x 4ft wide , express lube $40.95, automatic transmission $129.95, radiator $109.95, Kestra Gold express lube $79.95, std trans/ diff $79.95, tuneup 4cyl $149.95, 6cyl $175.95 ,

```html
<!DOCTYPE html>
<html lang="en">
<head>
<meta charset="utf-8">
<title>Service Price Sign</title>
<link rel="stylesheet" href="https://fonts.googleapis.com/css2?family=Poppins:wght@400;500;700;800&family=Oswald:wght@600&family=Sniglet&display=swap">
<style>
  :root {
    --blue: #0d56a5;
    --red: #c10d0e;
    --blue-shade: #13285a;
    --red-shade: #5b0a0b;
    --white: #ffffff;
    --ink: #1b1f3a;
    --backdrop: #e9e9e9;
  }
  * { box-sizing: border-box; margin: 0; padding: 0; }
  html, body { width: 1200px; height: 727px; overflow: hidden; }
  body {
    background: var(--backdrop);
    font-family: "Poppins", sans-serif;
    color: var(--white);
    position: relative;
  }
  .sign {
    position: absolute;
    left: 30px; top: 78px;
    width: 1140px; height: 570px;
    display: grid;
    grid-template-columns: repeat(3, 380px);
    grid-template-rows: repeat(2, 285px);
  }
  .tile { position: relative; overflow: hidden; --rule: 166px; }
  .tile--blue { background: var(--blue); --shade: var(--blue-shade); }
  .tile--red { background: var(--red); --shade: var(--red-shade); }
  .tile * { text-shadow: 2px 2px 0 var(--shade); }

  .head {
    position: absolute; left: 0; right: 0; top: 0; height: var(--rule);
    display: flex; flex-direction: column; align-items: center; justify-content: center;
    text-align: center; line-height: .95; padding-top: 6px;
  }
  .head .light { font-weight: 400; }
  .head .heavy { font-weight: 800; }

  .rule { position: absolute; left: 0; right: 0; top: var(--rule); height: 1px; background: var(--white); }
  .pill {
    position: absolute; left: 50%; top: var(--rule);
    transform: translate(-50%, -50%);
    background: var(--white); color: var(--ink);
    border-radius: 16px; height: 28px; padding: 0 14px;
    font-family: "Oswald", sans-serif; font-weight: 600; font-size: 19px;
    display: flex; align-items: center; white-space: nowrap;
    box-shadow: 2px 2px 0 var(--shade);
  }
  .pill, .pill * { text-shadow: none; }
  .miles {
    position: absolute; left: 0; right: 0; top: calc(var(--rule) + 22px);
    text-align: center; font-family: "Sniglet", sans-serif; font-size: 17px;
  }
  .price {
    position: absolute; left: 0; right: 0; top: calc(var(--rule) + 44px);
    display: flex; justify-content: center; align-items: flex-start;
    font-weight: 500; line-height: 1;
  }
  .price .from { font-family: "Sniglet", sans-serif; font-size: 11px; margin: 4px 4px 0 0; }
  .price .cur { font-size: 30px; margin-top: 6px; margin-right: 2px; }
  .price .amt { font-size: 58px; letter-spacing: -2px; }
  .price .tax { font-size: 11px; align-self: flex-end; margin: 0 0 6px 4px; }

  .brand-line { display: flex; align-items: center; gap: 7px; margin: 4px 0 6px; }
  .brand-line .mark { width: 20px; height: 20px; background: var(--white); }
  .brand-line .brand { font-weight: 800; font-size: 28px; text-shadow: none; }
  .brand-line .mark { box-shadow: none; }

  .split {
    position: absolute; left: 0; right: 0; top: calc(var(--rule) + 50px);
    display: flex; justify-content: center;
  }
  .split .option { width: 170px; display: flex; flex-direction: column; align-items: center; }
  .split .divider { width: 1px; background: var(--white); height: 62px; margin-top: 6px; }
  .split .cyl {
    font-weight: 800; font-size: 26px; line-height: 1; padding: 0 8px 1px 24px;
    border-bottom: 1px solid var(--white);
  }
  .split .price { position: static; margin-top: 0; }
  .split .price .from { margin-top: -8px; }
  .split .price .cur { font-size: 22px; margin-top: 4px; }
  .split .price .amt { font-size: 36px; letter-spacing: -1px; }
  .split .price .tax { font-size: 8px; margin-bottom: 4px; }
</style>
</head>
<body>
<main class="sign">

  <section class="tile tile--blue">
    <div class="head">
      <span class="heavy" style="font-size:40px;font-weight:700">EXPRESS</span>
      <span class="heavy" style="font-size:88px;letter-spacing:-2px">LUBE</span>
    </div>
    <div class="rule"></div>
    <div class="pill">14 POINT SERVICE</div>
    <p class="miles">Service Every 30 Miles</p>
    <div class="price"><span class="from">From</span><span class="cur">$</span><span class="amt">40.95</span><span class="tax">plus tax</span></div>
  </section>

  <section class="tile tile--red">
    <div class="head" style="padding-top:14px">
      <span class="light" style="font-size:48px">AUTOMATIC</span>
      <span class="heavy" style="font-size:38px;letter-spacing:-1px">TRANSMISSION</span>
    </div>
    <div class="rule"></div>
    <div class="pill">30 MINUTE SERVICE</div>
    <p class="miles">Service Every 25,000 Miles</p>
    <div class="price"><span class="from">From</span><span class="cur">$</span><span class="amt">129.95</span><span class="tax">plus tax</span></div>
  </section>

  <section class="tile tile--blue">
    <div class="head">
      <span class="light" style="font-size:50px">RADIATOR</span>
      <span class="heavy" style="font-size:64px;letter-spacing:-1px">SERVICE</span>
    </div>
    <div class="rule"></div>
    <div class="pill">30 MINUTE SERVICE</div>
    <p class="miles">Service Every 30 Miles</p>
    <div class="price"><span class="from">From</span><span class="cur">$</span><span class="amt">109.95</span><span class="tax">plus tax</span></div>
  </section>

  <section class="tile tile--red" style="--rule:170px">
    <div class="head">
      <span class="heavy" style="font-size:36px;font-weight:700">VOLTA'S BEST</span>
      <div class="brand-line"><span class="mark"></span><span class="brand">KESTRA GOLD</span></div>
      <span class="heavy" style="font-size:40px">EXPRESS LUBE</span>
    </div>
    <div class="rule"></div>
    <div class="pill">14 POINT SERVICE</div>
    <p class="miles">Service Every 3000 Miles</p>
    <div class="price"><span class="from">From</span><span class="cur">$</span><span class="amt">79.95</span><span class="tax">plus tax</span></div>
  </section>

  <section class="tile tile--blue" style="--rule:172px">
    <div class="head" style="line-height:.9">
      <span class="heavy" style="font-size:30px">STANDARD</span>
      <span class="heavy" style="font-size:30px">TRANSMISSION</span>
      <span style="font-family:'Sniglet',sans-serif;font-size:18px">or</span>
      <span class="heavy" style="font-size:30px">DIFFERENTIAL</span>
      <span class="heavy" style="font-size:30px">SERVICE</span>
    </div>
    <div class="rule"></div>
    <div class="pill">15 MINUTE SERVICE</div>
    <p class="miles">Service Every 25,000 Miles</p>
    <div class="price"><span class="from">From</span><span class="cur">$</span><span class="amt">79.95</span><span class="tax">plus tax</span></div>
  </section>

  <section class="tile tile--red" style="--rule:136px">
    <div class="head">
      <span class="heavy" style="font-size:38px;font-weight:700">VOLTA'S</span>
      <span class="heavy" style="font-size:62px">TUNE UP</span>
    </div>
    <div class="rule"></div>
    <div class="pill">60 MINUTE SERVICE</div>
    <p class="miles">Service Every 25,000 Miles</p>
    <div class="split">
      <div class="option">
        <span class="cyl">4 CYL</span>
        <div class="price"><span class="from">From</span><span class="cur">$</span><span class="amt">149.95</span><span class="tax">plus tax</span></div>
      </div>
      <div class="divider"></div>
      <div class="option">
        <span class="cyl">6 CYL</span>
        <div class="price"><span class="from">From</span><span class="cur">$</span><span class="amt">175.95</span><span class="tax">plus tax</span></div>
      </div>
    </div>
  </section>

</main>
</body>
</html>
```